"MEET THE TEAM" page web design

We need a "meet the team" page for our website!
Please look at our website to see the style we need

We are looking for something unique, fun, cool, technology-style and yet professional. We plan on taking a picture of each employee (not sure if this will be a real photo/caricature/ black and white/goofy picture--> but we are open to any ideas you have that will work with the design) and putting it there, along with a little bio about each person.

Thanks! looking forward to working together:)
Updates

Project Deadline Extended
Reason: I am excited to see more designs and find the perfect fit. Thanks designers :)

Target Market(s)

People looking to purchase servers, workstations, components

Industry/Entity Type

Information Technology

Number of Pages Required

1 page

Font styles to use
Sans Serif
Other font styles liked:
• The font we use on our site so it matches

Requirements
Must have
• please look at our website qondimex.com and see the theme and colors we want.
• We have 13 employees but would like to have a design where we can add/remove people if we hire/terminate them without messing up the design.
• We are looking for something unique, fun, cool, technology-style and yet professional. We plan on taking a picture of each employee (not sure if this will be a real photo/caricature/ black and white/goofy picture--> but we are open to any ideas you have that will work with the design) and putting it there, along with a little bio about each person.
• We can upload anything you need
Nice to have
• We are also interested in having a design where when the cursor moves over a person then the bio comes out or moves around, or something. (This is not required, but we would love some cool ideas) And if you can come up with some design, we would have our programmers create it for us.
Should not have
• we are open to anything

```html
<!DOCTYPE html>
<html lang="en">
<head>
<meta charset="utf-8">
<title>Meet the Team — Qondimex</title>
<link href="https://fonts.googleapis.com/css2?family=Open+Sans:ital,wght@0,400;0,600;0,700;1,600&family=Arimo:wght@400;700&display=swap" rel="stylesheet">
<style>
:root{
  --teal:#00c7b9;
  --teal-dark:#00a99d;
  --ink:#1a1a1a;
  --body:#555;
  --nav-bg:#e6e6e6;
  --panel:#f7f7f7;
  --footer:#a8a8a8;
  --footer-dark:#9b9b9b;
  --white:#fff;
}
*{box-sizing:border-box;margin:0;padding:0}
html,body{width:1140px;height:1200px;overflow:hidden;background:var(--white)}
body{position:relative;font-family:"Open Sans",sans-serif;color:var(--body)}
.abs{position:absolute}
.site-header{position:absolute;left:0;top:0;width:1140px;height:68px;background:var(--white)}
.brand{left:60px;top:12px;display:flex;align-items:center;gap:10px}
.brand-mark{width:36px;height:36px;background:var(--teal);border-radius:50%}
.brand-name{font-family:"Arimo",sans-serif;font-size:26px;color:var(--teal);letter-spacing:2px}
.account-pill{left:952px;top:0;width:130px;height:22px;border-radius:0 0 14px 14px;background:#c9c9c9;font-family:"Arimo",sans-serif;font-size:7px;color:#666;display:flex}
.account-pill span{flex:1;text-align:center;line-height:22px}
.account-pill span+span{background:#b3b3b3;border-radius:0 0 14px 0}
.contact-chip{top:31px;display:flex;align-items:center;gap:6px;font-family:"Arimo",sans-serif;color:#666}
.chip-icon{width:28px;height:28px;border:1.5px solid #b8ece8;border-radius:50%;display:flex;align-items:center;justify-content:center}
.main-nav{left:0;top:68px;width:1140px;height:24px;background:var(--nav-bg)}
.main-nav ul{position:absolute;left:61px;top:7px;list-style:none;display:flex;gap:7px;font-family:"Arimo",sans-serif;font-size:8.5px;color:#444}
.search{left:878px;top:69px;width:152px;height:21px;border-radius:11px;background:var(--white);border:1px solid #ddd;font-family:"Arimo",sans-serif;font-size:7.5px;color:#444;padding:5px 0 0 18px}
.cart{left:1045px;top:68px;width:24px;height:24px;border-radius:50%;background:var(--white);border:1px solid #ccc;display:flex;align-items:center;justify-content:center}
.breadcrumb-bar{left:0;top:92px;width:1140px;height:24px;background:linear-gradient(90deg,var(--teal-dark),var(--teal) 50%,var(--teal-dark))}
.breadcrumb{position:absolute;left:121px;top:7px;font-family:"Arimo",sans-serif;font-size:8px;font-weight:700;color:var(--white)}
.breadcrumb b{color:#0b3b38}
.intro-title{left:151px;top:150px;font-size:17px;font-weight:400;color:var(--ink)}
.intro-title span{color:var(--teal)}
.intro-text{left:149px;top:190px;width:480px;font-size:11px;line-height:17.4px}
.intro-text p+p{margin-top:17px}
.intro-media{left:659px;top:154px;width:332px;height:216px;background:linear-gradient(135deg,#c9a57f,#e3c9a9 55%,#b88e66)}
.media-arrow{top:84px;width:20px;height:42px;background:rgba(0,0,0,.35);color:#ddd;font-size:10px;display:flex;align-items:center;justify-content:center}
.team-panel{left:0;top:407px;width:1140px;height:413px;background:var(--panel);border-top:2px solid #ccc;border-bottom:2px solid #ccc}
.member-photo{left:149px;top:446px;width:186px;height:190px;background:linear-gradient(160deg,#e4e4e4,#8d8d8d 60%,#5b5b5b)}
.member-name{left:369px;top:441px;font-size:22px;font-weight:700;color:var(--ink)}
.member-role{left:370px;top:470px;font-size:14px;font-style:italic;font-weight:600;color:var(--teal)}
.member-contact{left:370px;top:496px;font-size:8.5px;color:#333;display:flex;gap:14px;align-items:center}
.member-contact span{display:flex;align-items:center;gap:5px}
.member-bio{left:369px;top:514px;width:330px;font-size:11px;line-height:17.4px;color:#444}
.social-square{top:615px;width:20px;height:20px;background:#111;display:flex;align-items:center;justify-content:center}
.skills-title{left:730px;top:441px;font-size:22px;font-weight:700;color:var(--ink)}
.skill-bar{left:730px;width:262px;height:26px;background:#ececec;border:1px solid #ddd}
.skill-fill{height:100%;background:var(--teal);color:var(--white);font-size:10px;display:flex;justify-content:space-between;align-items:center;padding:0 5px}
.skill-fill i{font-size:9.5px}
.slide-arrow{top:578px;width:20px;height:43px;background:#111;color:var(--white);font-size:11px;display:flex;align-items:center;justify-content:center}
.team-rule{left:224px;top:681px;width:699px;height:1px;background:#ddd}
.thumbs{left:289px;top:718px;display:flex;gap:17px}
.thumb{width:65px;height:65px;background:linear-gradient(160deg,#ededed,#8a8a8a)}
.thumb.is-active{background:linear-gradient(160deg,#7fe0d8,#1fb3a7)}
.site-footer{left:0;top:886px;width:1140px;height:314px;background:var(--footer);font-family:"Arimo",sans-serif;color:var(--white)}
.footer-about{position:absolute;left:335px;top:13px;width:530px;text-align:center;font-size:10.2px;line-height:13.3px}
.footer-rule{position:absolute;height:1px;background:rgba(255,255,255,.5)}
.footer-contact{position:absolute;top:86px;font-size:10.5px;line-height:13.3px;display:flex;gap:8px}
.footer-links{position:absolute;top:132px;font-size:12px;line-height:14px}
.footer-sub{position:absolute;left:738px;top:150px;width:110px;text-align:center;font-size:7px;line-height:9.6px}
.footer-base{position:absolute;left:0;top:194px;width:1140px;height:120px;background:var(--footer-dark)}
.round-social{position:absolute;top:12px;width:26px;height:26px;border:1px solid rgba(255,255,255,.7);border-radius:50%;display:flex;align-items:center;justify-content:center}
.copyright{position:absolute;left:520px;top:55px;font-size:9px;line-height:12px;display:flex;gap:6px;align-items:center}
.copyright i{width:14px;height:14px;background:var(--white);display:block}
.chat-now{left:987px;top:1182px;width:143px;height:18px;background:var(--teal);color:var(--white);font-family:"Arimo",sans-serif;font-size:9px;font-weight:700;padding:3px 0 0 6px}
</style>
</head>
<body>
<header class="site-header">
  <div class="abs brand"><span class="brand-mark"></span><span class="brand-name">QONDIMEX</span></div>
  <div class="abs account-pill"><span>SIGN UP</span><span>LOGIN</span></div>
  <div class="abs contact-chip" style="left:877px;font-size:9px">
    <span class="chip-icon"><svg width="12" height="10" viewBox="0 0 12 10"><path d="M1 1h8v5H4L2 8V6H1z" fill="var(--teal)"/></svg></span>LIVE CHAT
  </div>
  <div class="abs contact-chip" style="left:970px;font-size:12px">
    <span class="chip-icon"><svg width="11" height="11" viewBox="0 0 12 12"><path d="M2 1l2.5 0 1 3-1.5 1a7 7 0 0 0 3 3l1-1.5 3 1V10a1 1 0 0 1-1 1C5 11 1 7 1 2a1 1 0 0 1 1-1z" fill="var(--teal)"/></svg></span>555-014-2290
  </div>
</header>
<nav class="abs main-nav">
  <ul><li>SERVERS ▾</li><li>WORKSTATIONS ▾</li><li>COMPONENTS</li><li>VIRTUAL REALITY</li><li>DRONES</li><li>ABOUT US</li><li>BLOG</li><li>RESOURCES ▾</li><li>CONTACT US</li></ul>
</nav>
<div class="abs search">Search<svg style="position:absolute;right:9px;top:5px" width="10" height="10" viewBox="0 0 10 10"><circle cx="4" cy="4" r="3" fill="none" stroke="var(--teal)" stroke-width="1.6"/><path d="M6.2 6.2L9 9" stroke="var(--teal)" stroke-width="1.8"/></svg></div>
<div class="abs cart"><svg width="11" height="10" viewBox="0 0 11 10"><rect x="1" y="2" width="9" height="7" rx="1" fill="var(--teal)"/></svg></div>
<div class="abs breadcrumb-bar"><div class="breadcrumb">HOME / <b>CONTACT US</b></div></div>

<main>
<section>
  <h1 class="abs intro-title">MEET THE <span>TEAM</span></h1>
  <div class="abs intro-text">
    <p>Lorem ipsum dolor sit amet, consectetur adipiscing elit. Curabitur pellentesque neque eget diam posuere porta. Quisque ut nulla at nunc vehicula lacinia. Proin adipiscing porta tellus, ut feugiat nibh adipiscing sit amet. In eu justo a felis faucibus ornare vel id viverra leo. Nullam convallis, arcu vel pellentesque sodales, nisi est varius diam, ac ultrices sem ante quis sem. Proin ultricies volutpat sapien, nec scelerisque ligula mollis lobortis.</p>
    <p>Curabitur pellentesque neque eget diam posuere porta. Quisque ut nulla at nunc vehicula lacinia.&nbsp; Vestibulum ante ipsum primis in faucibus orci luctus et ultrices posuere ipsum primis in faucibus orci luctus.</p>
  </div>
  <div class="abs intro-media" role="img" aria-label="Photo of a tablet showing the team page, lying on a wooden desk beside notebooks and a pen">
    <span class="abs media-arrow" style="left:0">&lt;</span><span class="abs media-arrow" style="right:0">&gt;</span>
  </div>
</section>

<section class="abs team-panel"></section>
<div class="abs slide-arrow" style="left:61px">&lt;</div>
<div class="abs slide-arrow" style="left:1060px">&gt;</div>
<div class="abs member-photo" role="img" aria-label="Black and white portrait of team member Marcel Ostrand"></div>
<h2 class="abs member-name">Marcel Ostrand.</h2>
<div class="abs member-role">Front End</div>
<div class="abs member-contact">
  <span><svg width="13" height="9" viewBox="0 0 13 9"><rect width="13" height="9" fill="#777"/><path d="M0 0l6.5 5L13 0" stroke="#fff" fill="none"/></svg>MarcelO@qondimex.com</span>
  <span><svg width="7" height="11" viewBox="0 0 7 11"><rect x=".5" y=".5" width="6" height="10" rx="1" fill="none" stroke="#555"/></svg>+ (555) 010 48273</span>
</div>
<p class="abs member-bio">Inani nominati sit eu. Te ubique cotidieque philosophia mel, vix id omnes iudico prompta. Ex usu nihil mediocritatem. Sea quod vituperata no, omittam offendit vel in. Noster voluptua luptatum id mea. Et voluptatum adversarium usu, rebum nominati recte-que vix ei.</p>
<span class="abs social-square" style="left:370px" aria-label="Share profile"><svg width="10" height="10" viewBox="0 0 10 10"><circle cx="2" cy="5" r="1.5" fill="#fff"/><circle cx="8" cy="2" r="1.5" fill="#fff"/><circle cx="8" cy="8" r="1.5" fill="#fff"/><path d="M2 5L8 2M2 5l6 3" stroke="#fff" stroke-width="1"/></svg></span>
<span class="abs social-square" style="left:406px" aria-label="Profile link"><svg width="11" height="11" viewBox="0 0 11 11"><path d="M4.5 6.5l2-2M3.5 5L2 6.5a2 2 0 0 0 2.5 2.5L6 7.5M7.5 6L9 4.5A2 2 0 0 0 6.5 2L5 3.5" stroke="#fff" stroke-width="1.3" fill="none"/></svg></span>

<h2 class="abs skills-title">Skills</h2>
<div class="abs skill-bar" style="top:484px"><div class="skill-fill" style="width:194px">PHP <i>80%</i></div></div>
<div class="abs skill-bar" style="top:521px"><div class="skill-fill" style="width:177px">PHP <i>70%</i></div></div>
<div class="abs skill-bar" style="top:560px"><div class="skill-fill" style="width:139px">PHP <i>50%</i></div></div>

<div class="abs team-rule"></div>
<div class="abs thumbs">
  <div class="thumb" role="img" aria-label="Team member portrait"></div>
  <div class="thumb" role="img" aria-label="Team member portrait"></div>
  <div class="thumb" role="img" aria-label="Team member portrait"></div>
  <div class="thumb is-active" role="img" aria-label="Selected team member portrait"></div>
  <div class="thumb" role="img" aria-label="Team member portrait"></div>
  <div class="thumb" role="img" aria-label="Team member portrait"></div>
  <div class="thumb" role="img" aria-label="Team member portrait"></div>
</div>
</main>

<footer class="abs site-footer">
  <p class="footer-about">Based in Harbor Vale California, Qondimex offers custom servers, storage, and workstations for local businesses in Los Angeles, Beverly Hills, Thousand Oaks, Ventura, Orange County, Santa Barbara, Oxnard, Irvine, Anaheim, and San Diego. Qondimex also offers such products to clients throughout the United States and Worldwide.</p>
  <div class="footer-rule" style="left:340px;top:72px;width:540px"></div>
  <div class="footer-contact" style="left:357px">
    <svg width="8" height="11" viewBox="0 0 8 11"><path d="M4 11L1 5a3 3 0 1 1 6 0z" fill="#fff"/></svg><span>4180 Linden Row<br>Harbor Vale, CA 90000</span></div>
  <div class="footer-contact" style="left:535px">
    <svg width="10" height="10" viewBox="0 0 12 12"><path d="M2 1l2.5 0 1 3-1.5 1a7 7 0 0 0 3 3l1-1.5 3 1V10a1 1 0 0 1-1 1C5 11 1 7 1 2a1 1 0 0 1 1-1z" fill="#fff"/></svg><span>555-014-2290</span></div>
  <div class="footer-contact" style="left:689px">
    <svg width="11" height="9" viewBox="0 0 13 9"><rect width="13" height="9" fill="#fff"/><path d="M0 0l6.5 5L13 0" stroke="#a8a8a8" fill="none"/></svg><span>sales@qondimex.com</span></div>
  <span class="footer-links" style="left:297px">Computer Hardware</span>
  <span class="footer-links" style="left:450px">Drones</span>
  <span class="footer-links" style="left:525px">Virtual Reality</span>
  <span class="footer-links" style="left:641px">About Us</span>
  <span class="footer-links" style="left:746px">Customer Support</span>
  <div class="footer-sub">Terms and Conditions<br>Warranty Information<br>Contact Us<br>Return Policy</div>
  <div class="footer-base">
    <span class="round-social" style="left:497px" aria-label="Share"><svg width="11" height="11" viewBox="0 0 10 10"><circle cx="2" cy="5" r="1.4" fill="#fff"/><circle cx="8" cy="2" r="1.4" fill="#fff"/><circle cx="8" cy="8" r="1.4" fill="#fff"/><path d="M2 5L8 2M2 5l6 3" stroke="#fff" stroke-width=".9"/></svg></span>
    <span class="round-social" style="left:533px" aria-label="Website"><svg width="12" height="12" viewBox="0 0 12 12"><circle cx="6" cy="6" r="5" fill="none" stroke="#fff"/><ellipse cx="6" cy="6" rx="2.2" ry="5" fill="none" stroke="#fff"/><path d="M1 6h10" stroke="#fff"/></svg></span>
    <span class="round-social" style="left:569px" aria-label="Chat"><svg width="12" height="11" viewBox="0 0 12 10"><path d="M1 1h10v6H5L2.5 9V7H1z" fill="none" stroke="#fff"/></svg></span>
    <span class="round-social" style="left:605px" aria-label="Email"><svg width="12" height="9" viewBox="0 0 13 9"><rect x=".5" y=".5" width="12" height="8" fill="none" stroke="#fff"/><path d="M.5 .5l6 4.5 6-4.5" stroke="#fff" fill="none"/></svg></span>
    <div class="footer-rule" style="left:170px;top:55px;width:830px"></div>
    <div class="copyright" style="top:64px"><i></i><span>Qondimex, LLC.<br>Copyright © 2017</span></div>
  </div>
</footer>
<div class="abs chat-now">CHAT NOW</div>
</body>
</html>
```